Bold Modern Creative Wine Label Needed for a Chardonnay

We need a modern, eye catching label, one that will appeal to millennials, but also attract the older more conservative crowd. We like the boldness of black on white but are open to your suggestions. Since the bottle type is a light green 'burgundy style' bottle, you should take that into account. The name of the brand is Vo`. The attached label is example of what we like very much. It is eye catching and bold and modern. Keep in mind that the bottle will be light green in color so black and white might not work so well. Use your creativity please! The label can be any size but needs to fit on this shape bottle. See attached photos. thanks!!

(Please no grapes or wine glasses or wine bottles featured on the label!)
Updates

Hi Designers, I just wanted to let you know that we received many great designs and we are sorting through them this week. The website is making it a bit difficult to create a 'poll' so this is taking longer than we expected. Thanks for all the great submissions!

```html
<!DOCTYPE html>
<html lang="en">
<head>
<meta charset="utf-8">
<title>Vo` Chardonnay 2019 Label</title>
<link rel="stylesheet" href="https://fonts.googleapis.com/css2?family=Bodoni+Moda:opsz,wght@6..96,400&display=swap">
<style>
  :root {
    --label-paper: #ffffff;
    --label-ink: #000000;
    --rule-ink: #333333;
  }
  html, body {
    margin: 0;
    padding: 0;
    width: 1200px;
    height: 1050px;
    overflow: hidden;
    background: var(--label-paper);
  }
  .label {
    position: relative;
    width: 1200px;
    height: 1050px;
    background: var(--label-paper);
    font-family: "Bodoni Moda", "Didot", serif;
    color: var(--label-ink);
  }
  .wordmark {
    position: absolute;
    left: 0;
    top: 0;
    width: 1200px;
    height: 760px;
  }
  .wordmark text {
    font-family: "Bodoni Moda", "Didot", serif;
    font-weight: 400;
    fill: var(--label-ink);
  }
  .varietal-rule {
    position: absolute;
    left: 352px;
    top: 900px;
    width: 552px;
    height: 2px;
    background: var(--rule-ink);
  }
  .varietal {
    position: absolute;
    left: 420px;
    width: 400px;
    top: 876px;
    margin: 0;
    text-align: center;
    font-size: 44px;
    font-weight: 400;
    line-height: 44px;
  }
  .vintage {
    position: absolute;
    left: 432px;
    width: 400px;
    top: 940px;
    margin: 0;
    text-align: center;
    font-size: 54px;
    font-weight: 400;
    line-height: 54px;
  }
</style>
</head>
<body>
  <main class="label">
    <svg class="wordmark" viewBox="0 0 1200 760" role="img" aria-label="Vo`">
      <text class="wordmark-name" x="352" y="690" font-size="560" textLength="553" lengthAdjust="spacingAndGlyphs">Vo`</text>
    </svg>
    <div class="varietal-rule"></div>
    <p class="varietal">chardonnay</p>
    <p class="vintage">2019</p>
  </main>
</body>
</html>
```